Flyer-Design für eine Band
Zielgruppe
Bandname 'Tanzfeld'
Musiker
Coverband für Hochzeiten, Events und Partymusik
Zielgruppe sind Leute (jung und alt) die stimmungsvolle Musik für Ihre Veranstaltung suchen
Aufgabenstellung
Die Werbekarte soll zu unserem bisherigen Stil laut Social Media bzw. Homepage passen.
Wir möchen gerne unser(e) Foto(s) aus unserem Fotoshooting verwenden.
Wir hätten gerne eine Werbekarte im Postkartenformat (vorne und hinten bedruckt)
Angeführt soll sein:
- die Webseite (https://tanzfeld-musik.at)
- email (info@tanzfeld-musik.at)
- Telefonnummer (0677 482 19 736)

```html
<!DOCTYPE html>
<html lang="de">
<head>
<meta charset="utf-8">
<title>Tanzfeld – Werbekarte</title>
<link href="https://fonts.googleapis.com/css2?family=Dancing+Script:wght@700&family=Norican&family=Lustria&family=Crimson+Text:wght@600&display=swap" rel="stylesheet">
<style>
  :root {
    --teal: #2aa5a8;
    --teal-dark: #24707a;
    --ink: #2b5963;
    --paper: #f6f6f6;
    --circle-top: #9c9fc6;
    --circle-bottom: #3b8ea5;
    --white-soft: #eef6f7;
    --stage: #dcdde1;
    --gold: #c9b44a;
  }
  * { box-sizing: border-box; margin: 0; padding: 0; }
  html, body { width: 1200px; height: 2554px; overflow: hidden; }
  body { background: var(--stage); position: relative; font-family: "Norican", cursive; }

  .card { position: absolute; left: 0; width: 1200px; background: var(--paper); overflow: hidden; }
  .card--front { top: 0; height: 855px; }
  .card--back { top: 855px; height: 858px; border-right: 4px solid var(--gold); }

  .brand { position: absolute; display: flex; align-items: center; gap: 14px; z-index: 2; }
  .brand--front { left: 30px; top: 36px; }
  .brand--back { left: 28px; top: 36px; }
  .brand__dot { width: 40px; height: 40px; border-radius: 50%; border: 3px solid var(--teal); opacity: .6; }
  .brand__name { font-family: "Lustria", serif; font-size: 40px; line-height: 1; color: var(--teal); opacity: .7; }

  .photo--duo-standing { position: absolute; left: 600px; top: 70px; width: 600px; height: 785px;
    background: linear-gradient(180deg, #f1f1f1 0%, #e2e2e4 70%, #c9ab8c 92%, #b99a7c 100%); }

  .halo { position: absolute; }
  .halo--front { left: -60px; top: 295px; width: 740px; height: 740px; }
  .halo--back { left: -40px; top: 300px; width: 710px; height: 710px; }

  .title { position: absolute; left: 165px; top: 120px; font-family: "Dancing Script", cursive; font-weight: 700;
    font-size: 200px; line-height: 1.1; color: var(--teal); white-space: nowrap;
    transform: rotate(-8deg); transform-origin: left center; z-index: 1; }

  .tagline { position: absolute; left: 75px; width: 450px; text-align: center; color: var(--white-soft);
    font-size: 42px; line-height: 1.25; transform: rotate(-8deg); }
  .tagline--one { top: 395px; }
  .tagline--two { top: 630px; width: 470px; left: 70px; }

  .names { position: absolute; left: 362px; top: 130px; color: var(--teal); font-family: "Dancing Script", cursive;
    font-weight: 700; font-size: 80px; line-height: 1.1; white-space: nowrap; }
  .names small { font-family: "Norican", cursive; font-weight: 400; font-size: 32px; }

  .offer__title { position: absolute; left: 525px; top: 312px; font-size: 46px; font-weight: 400; color: var(--teal-dark); white-space: nowrap; }
  .offer__list { position: absolute; left: 588px; top: 398px; list-style: none; color: var(--ink); font-size: 30px; line-height: 32px; white-space: nowrap; }
  .offer__list li::first-letter { color: var(--teal); font-size: 33px; }
  .offer__list .i1 { padding-left: 24px; }
  .offer__list .i2 { padding-left: 42px; }
  .offer__list .i3 { padding-left: 58px; }
  .offer__list .i4 { padding-left: 70px; }
  .offer__list .i5 { padding-left: 78px; }
  .offer__list .i6 { padding-left: 84px; }
  .offer__list .i7 { padding-left: 88px; }

  .contact { position: absolute; left: 935px; top: 712px; list-style: none; font-family: "Crimson Text", serif;
    font-weight: 600; font-size: 20px; color: var(--ink); white-space: nowrap; }
  .contact li { display: flex; align-items: center; gap: 10px; height: 39px; }
  .contact svg { width: 26px; height: 26px; flex: none; }
</style>
</head>
<body>

<section class="card card--front">
  <div class="photo--duo-standing" role="img" aria-label="Foto: Sängerin mit Mikrofon und Gitarrist mit Akustikgitarre stehen nebeneinander"></div>
  <svg class="halo halo--front" viewBox="0 0 740 740" aria-hidden="true">
    <defs>
      <linearGradient id="haloFront" x1="0" y1="0" x2="0" y2="1">
        <stop offset="0" stop-color="var(--circle-top)"/>
        <stop offset=".55" stop-color="#5c9fb4"/>
        <stop offset="1" stop-color="var(--circle-bottom)"/>
      </linearGradient>
    </defs>
    <circle cx="370" cy="370" r="370" fill="url(#haloFront)"/>
  </svg>
  <div class="brand brand--front"><span class="brand__dot"></span><span class="brand__name">tanzfeld</span></div>
  <h1 class="title">Tanzfeld</h1>
  <p class="tagline tagline--one">Gute Hochzeitssänger gibt es viele, Tanzfeld nur einmal!</p>
  <p class="tagline tagline--two">Euer perfekter Tag…<br>die perfekte musikalische Begleitung von uns!</p>
</section>

<section class="card card--back">
  <div class="brand brand--back"><span class="brand__dot"></span><span class="brand__name">tanzfeld</span></div>
  <svg class="halo halo--back" viewBox="0 0 710 710" role="img" aria-label="Foto: Porträt des Duos, Gitarrist und Sängerin nebeneinander">
    <defs>
      <linearGradient id="haloBack" x1="0" y1="0" x2="1" y2="1">
        <stop offset="0" stop-color="#8f8fbf"/>
        <stop offset=".6" stop-color="#6d9cb6"/>
        <stop offset="1" stop-color="#b9c5d6"/>
      </linearGradient>
    </defs>
    <circle cx="355" cy="355" r="355" fill="url(#haloBack)"/>
  </svg>
  <h2 class="names"><small>with</small> Sabine <small>and</small> Thomas</h2>
  <h3 class="offer__title">Was wir euch anbieten?</h3>
  <ul class="offer__list">
    <li>Perfekte Abstimmung eurer Wünsche mit</li>
    <li class="i1">unserem Portfolio.</li>
    <li class="i2">Eigenes Equipment.</li>
    <li class="i3">Zuverlässigkeit.</li>
    <li class="i4">Professionelle Vorbereitung und Darbi-</li>
    <li class="i5">etung.</li>
    <li class="i6">Unkomplizierte Abwicklung.</li>
    <li class="i7">Fixpreis – keine versteckten Kosten.</li>
  </ul>
  <ul class="contact">
    <li><svg viewBox="0 0 26 26" aria-hidden="true"><circle cx="13" cy="13" r="13" fill="var(--teal)"/><path d="M9 7l3 3-1.5 2a9 9 0 0 0 4.5 4.5l2-1.5 3 3-2 2C12 19 7 14 7 9z" fill="#fff"/></svg>0677 482 19 736</li>
    <li><svg viewBox="0 0 26 26" aria-hidden="true"><circle cx="13" cy="13" r="13" fill="var(--teal)"/><rect x="6.5" y="8.5" width="13" height="9" fill="none" stroke="#fff" stroke-width="1.6"/><path d="M6.5 8.5l6.5 5 6.5-5" fill="none" stroke="#fff" stroke-width="1.6"/></svg>info@tanzfeld-musik.at</li>
    <li><svg viewBox="0 0 26 26" aria-hidden="true"><circle cx="13" cy="13" r="13" fill="var(--teal)"/><circle cx="13" cy="13" r="7" fill="none" stroke="#fff" stroke-width="1.5"/><ellipse cx="13" cy="13" rx="3" ry="7" fill="none" stroke="#fff" stroke-width="1.5"/><path d="M6 13h14" stroke="#fff" stroke-width="1.5"/></svg>https://tanzfeld-musik.at</li>
  </ul>
</section>

</body>
</html>
```